Brenwick Realty
Business cards and stationery
Brenwick Realty - Real Estate
Creative Brief
Modern
Marian Talcott
Director
Level 4 218 Garnet Lane Melbourne VIC 3000
marian@brenwickrealty-example.com.au
www.brenwickrealty-example.com.au
Brenwick Summit Realty 518902K Licensee Marian Talcott
Stationery needs to have the licensee info on the bottom of letterhead
black background logo in centre

```html
<!DOCTYPE html>
<html lang="en">
<head>
<meta charset="utf-8">
<title>Brenwick Realty – Business Card</title>
<link href="https://fonts.googleapis.com/css2?family=Open+Sans:wght@400;600;700;800&display=swap" rel="stylesheet">
<style>
  :root {
    --stage: #3a3a3c;
    --card-black: #111113;
    --card-blue-top: #5bb8ee;
    --card-blue-bottom: #1f6fb8;
    --pink: #e5358f;
    --cyan: #2cb7e6;
    --white: #ffffff;
    --grey-text: #d9d9d9;
    --rule: #8a8a8a;
    --art-tone-a: #3a1f31;
    --art-tone-b: #5a2a48;
  }
  * { margin: 0; padding: 0; box-sizing: border-box; }
  html, body { width: 1200px; height: 901px; overflow: hidden; }
  body {
    background: var(--stage);
    font-family: "Open Sans", Arial, sans-serif;
    position: relative;
  }
  .card {
    position: absolute;
    left: 250px;
    width: 700px;
    height: 400px;
    border-radius: 18px;
    overflow: hidden;
  }
  /* Back side */
  .card--back {
    top: 30px;
    background: linear-gradient(160deg, var(--card-blue-top), var(--card-blue-bottom));
    color: var(--white);
  }
  .back-brand {
    position: absolute;
    top: 150px; left: 0; right: 0;
    text-align: center;
    font-size: 52px;
    font-weight: 800;
    letter-spacing: 0.5px;
  }
  .back-web {
    position: absolute;
    top: 228px; left: 0; right: 0;
    text-align: center;
    font-size: 17px;
    font-weight: 600;
    letter-spacing: 1px;
  }
  .back-licensee {
    position: absolute;
    right: 28px; bottom: 22px;
    font-size: 12px;
    opacity: 0.9;
  }
  /* Front side */
  .card--front {
    top: 470px;
    background: var(--card-black);
    color: var(--grey-text);
  }
  .front-brand {
    position: absolute;
    top: 40px; left: 40px;
    display: flex; align-items: center; gap: 12px;
    font-size: 40px;
    font-weight: 800;
    color: var(--pink);
  }
  .front-brand .brand-dot {
    width: 18px; height: 18px; border-radius: 50%;
    background: var(--pink);
  }
  .contact {
    position: absolute;
    top: 132px; left: 40px;
    width: 380px;
  }
  .contact-name { font-size: 24px; font-weight: 700; color: var(--pink); line-height: 1.2; }
  .contact-role { font-size: 17px; font-weight: 600; color: var(--cyan); margin-bottom: 6px; }
  .contact-address { font-size: 16px; color: var(--white); line-height: 1.35; }
  .contact-rule { border-top: 2px dotted var(--rule); margin: 12px 0 10px; width: 330px; }
  .contact-list { list-style: none; }
  .contact-list li {
    display: flex; align-items: center; gap: 12px;
    font-size: 16px; color: var(--white); line-height: 1.55;
  }
  .contact-list svg { width: 16px; height: 16px; flex: none; }
  .art-area {
    position: absolute;
    right: 0; top: 0;
    width: 250px; height: 400px;
    background: linear-gradient(180deg, var(--art-tone-b), var(--art-tone-a));
  }
</style>
</head>
<body>

  <section class="card card--back" aria-label="Card back">
    <div class="back-brand">Brenwick Realty</div>
    <div class="back-web">www.brenwickrealty-example.com.au</div>
    <div class="back-licensee">Licensee Marian Talcott</div>
  </section>

  <section class="card card--front" aria-label="Card front">
    <div class="front-brand"><span class="brand-dot"></span>Brenwick Realty</div>

    <div class="contact">
      <div class="contact-name">Marian Talcott</div>
      <div class="contact-role">Director</div>
      <div class="contact-address">Level 4 218 Garnet Lane<br>Melbourne VIC 3000</div>
      <div class="contact-rule"></div>
      <ul class="contact-list">
        <li>
          <svg viewBox="0 0 16 16" aria-hidden="true"><path fill="#e5358f" d="M3 1h3l1 4-2 1c1 2 3 4 5 5l1-2 4 1v3c0 1-1 2-2 2C7 15 1 9 1 3c0-1 1-2 2-2z"/></svg>
          03 9555 0142
        </li>
        <li>
          <svg viewBox="0 0 16 16" aria-hidden="true"><rect x="4" y="0.5" width="8" height="15" rx="1.5" fill="#e5358f"/><rect x="5.5" y="2.5" width="5" height="9" fill="#111113"/></svg>
          0400 555 317
        </li>
        <li>
          <svg viewBox="0 0 16 16" aria-hidden="true"><rect x="1" y="6" width="14" height="8" rx="1" fill="#e5358f"/><rect x="4" y="1" width="8" height="6" fill="#e5358f"/><rect x="5" y="2" width="6" height="4" fill="#111113"/></svg>
          03 9555 0198
        </li>
        <li>
          <svg viewBox="0 0 16 16" aria-hidden="true"><rect x="1" y="3" width="14" height="10" rx="1" fill="#e5358f"/><path d="M1.5 3.5 8 9l6.5-5.5" stroke="#111113" stroke-width="1.4" fill="none"/></svg>
          marian@brenwickrealty-example.com.au
        </li>
      </ul>
    </div>

    <div class="art-area" role="img" aria-label="Area for a stylised city buildings illustration in pink, green and orange"></div>
  </section>

</body>
</html>
```